KELP clinical trial results infographic

We need an infographic which presents the results from the KELP research trial. It should be colourful and engaging, in understandable language and showing the steps to get to the results. This is to showcase the results to patients/the public/clinicians, giving a brief summary of what the study proved. The final design should have the KELP logo at the top (please see the logo on the attached Word document)
I have attached the required logos which need to be used (KELP - within the Word doc, Brindlemoor Injury and Acute Care, University of Caddering, QRV - see also their design pack attached) as well as an example from another study, PLUMBEX4, as an example of what the layout could look like. Please DO NOT use the content from the PLUMBEX4 example though, please instead use the content from the attached document 'InfographicDesignInformation_KELP_ArtHatchery_02Dec2025'. Please also include information about the funding in a footer at the bottom of the infographic (as per the above document).
Look and feel
Each slider illustrates characteristics of the customer's brand and the style your logo design should communicate.

```html
<!DOCTYPE html>
<html lang="en">
<head>
<meta charset="utf-8">
<title>KELP – Weight Bearing in Ankle Fractures</title>
<link href="https://fonts.googleapis.com/css2?family=Poppins:wght@400;500;600;700;800;900&display=swap" rel="stylesheet">
<style>
  :root {
    --blue: #0b4a93;
    --page: #b6b6b6;
    --card: #ffffff;
    --mist: #efefef;
    --band-grey: #e2e2e2;
    --label-grey: #bdbdbd;
    --ink: #1c1c1c;
    --illus-a: #e8ecf3;
    --illus-b: #c9d6ea;
  }
  * { margin: 0; padding: 0; box-sizing: border-box; }
  html, body { width: 694px; height: 1200px; overflow: hidden; }
  body { background: var(--page); font-family: "Poppins", sans-serif; color: var(--ink); position: relative; }
  .poster { position: absolute; left: 56px; top: 58px; width: 581px; height: 1084px; background: var(--card); overflow: hidden; }
  .abs { position: absolute; }

  .header { left: 0; top: 0; width: 581px; height: 128px; background: var(--mist); }
  .title-top { left: 27px; top: 20px; font-weight: 800; font-size: 40px; line-height: 1; color: var(--blue); letter-spacing: -0.4px; white-space: nowrap; }
  .title-band { left: 27px; top: 56px; width: 353px; height: 38px; background: var(--label-grey); color: #fff; font-weight: 800; font-size: 30px; line-height: 38px; padding-left: 8px; white-space: nowrap; letter-spacing: 0.2px; }
  .brand-name { left: 389px; top: 26px; width: 164px; text-align: center; font-weight: 800; font-size: 62px; line-height: 1; color: var(--blue); letter-spacing: 1px; }
  .subtitle { left: 27px; top: 104px; font-size: 11.9px; color: #222; white-space: nowrap; }

  .headline { left: 27px; top: 145px; font-weight: 700; font-size: 12.7px; color: var(--blue); white-space: nowrap; }
  .foot-illus { left: 0; top: 173px; width: 199px; height: 110px; background: linear-gradient(160deg, var(--illus-a), var(--illus-b)); }
  .big-s { left: 25px; top: 262px; font-weight: 900; font-size: 104px; line-height: 1; color: var(--blue); }
  .s-word { left: 87px; font-weight: 800; font-size: 21px; line-height: 1; color: var(--blue); }
  .summary { left: 214px; width: 340px; font-size: 8.75px; line-height: 13.4px; color: #222; }

  .wave { position: absolute; left: 0; width: 581px; height: 6px; display: block; }
  .key-band { left: 0; top: 386px; width: 581px; height: 98px; background: var(--blue); }
  .key-row { left: 27px; top: 399px; display: flex; gap: 8px; white-space: nowrap; }
  .key-box { background: #fff; color: var(--blue); font-weight: 800; font-size: 38px; line-height: 40px; padding: 0 4px; letter-spacing: -0.3px; }
  .key-findings { color: #fff; font-weight: 800; font-size: 38px; line-height: 40px; }
  .key-text { left: 29px; top: 450px; width: 535px; color: #fff; font-size: 8.9px; line-height: 13.6px; }

  .elig-title { left: 27px; top: 511px; font-weight: 800; font-size: 15.5px; line-height: 15px; color: var(--blue); }
  .elig-illus { left: 27px; top: 545px; width: 81px; height: 74px; background: linear-gradient(180deg, #f4f6fa, #dbe4f2); }
  .elig-tag { left: 27px; top: 620px; width: 81px; height: 16px; background: var(--label-grey); color: #fff; font-weight: 700; font-size: 9.5px; line-height: 16px; text-align: center; }
  .side-bar { width: 16px; background: var(--blue); color: #fff; font-weight: 700; font-size: 9px; display: flex; align-items: center; justify-content: center; }
  .side-bar span { transform: rotate(-90deg); white-space: nowrap; }
  .criteria { list-style: none; font-size: 8.6px; line-height: 11.6px; color: #222; }
  .criteria li { position: absolute; padding-left: 9px; white-space: nowrap; }
  .criteria li::before { content: ""; position: absolute; left: 0; top: 4px; width: 3px; height: 3px; border-radius: 50%; background: var(--blue); }

  .details-band { left: 0; top: 667px; width: 581px; height: 95px; background: var(--band-grey); }
  .details-illus { left: 30px; top: 675px; width: 69px; height: 50px; background: linear-gradient(180deg, #dfe5ef, #c6d2e6); }
  .details-title { left: 110px; top: 675px; font-weight: 800; font-size: 23px; line-height: 25px; color: var(--blue); }
  .details-tag { left: 26px; top: 733px; width: 217px; height: 19px; background: var(--label-grey); color: #fff; font-weight: 700; font-size: 10.5px; line-height: 19px; text-align: center; white-space: nowrap; }
  .details-list { font-size: 8.9px; }
  .details-list li { padding-left: 0; }
  .details-list li::before { left: -15px; top: 3px; width: 4px; height: 4px; }

  .info-card { top: 813px; width: 144px; height: 122px; background: var(--band-grey); border-radius: 3px; }
  .info-circle { top: 788px; width: 50px; height: 50px; border-radius: 50%; background: var(--blue); display: flex; align-items: center; justify-content: center; }
  .info-main { position: absolute; left: 0; top: 40px; width: 100%; text-align: center; color: var(--blue); font-weight: 700; font-size: 13.8px; line-height: 20px; }
  .info-main.contact { font-size: 11.2px; line-height: 14.5px; top: 44px; font-weight: 600; }
  .info-label { position: absolute; left: 0; bottom: 0; width: 100%; height: 20px; background: var(--blue); color: #fff; font-weight: 700; font-size: 9.5px; line-height: 20px; text-align: center; border-radius: 0 0 3px 3px; }

  .funding-band { left: 0; top: 960px; width: 581px; height: 58px; background: var(--blue); }
  .funding-text { left: 0; top: 972px; width: 581px; text-align: center; color: #fff; font-weight: 700; font-size: 11.4px; line-height: 15.5px; }

  .partner { display: flex; align-items: center; gap: 6px; color: #6b6b6b; font-size: 13px; font-weight: 400; white-space: nowrap; }
  .partner .mark { width: 22px; height: 22px; background: #7e7e7e; }
  .partner.uni .mark { width: 33px; height: 33px; background: #1b2755; }
  .partner.qrv { color: #1f3d7a; font-size: 18px; }
  .partner.qrv .mark { width: 34px; height: 34px; background: #f0a42c; }
</style>
</head>
<body>
<svg width="0" height="0" style="position:absolute">
  <defs>
    <pattern id="scallop-blue" width="20" height="6" patternUnits="userSpaceOnUse">
      <path d="M0 6 Q5 0 10 3 T20 3 V6 Z" fill="#0b4a93"/>
    </pattern>
    <pattern id="scallop-grey" width="20" height="6" patternUnits="userSpaceOnUse">
      <path d="M0 6 Q5 0 10 3 T20 3 V6 Z" fill="#e2e2e2"/>
    </pattern>
    <pattern id="scallop-white" width="20" height="6" patternUnits="userSpaceOnUse">
      <path d="M0 6 Q5 0 10 3 T20 3 V6 Z" fill="#ffffff"/>
    </pattern>
  </defs>
</svg>

<main class="poster">
  <header class="abs header"></header>
  <svg class="wave" style="top:122px" viewBox="0 0 581 6"><rect width="581" height="6" fill="url(#scallop-white)"/></svg>
  <h1 class="abs title-top">WEIGHT BEARING</h1>
  <div class="abs title-band">IN ANKLE FRACTURES</div>
  <div class="abs brand-name">KELP</div>
  <p class="abs subtitle">A randomised clinical trial of weight-bearing following operatively treated ankle fracture.</p>

  <h2 class="abs headline">PATIENTS CAN SAFELY START WALKING SOON AFTER SURGERY ON A BROKEN ANKLE</h2>
  <div class="abs foot-illus" role="img" aria-label="Illustration of a foot skeleton with a clinician, medical crosses and a tick"></div>
  <div class="abs big-s">S</div>
  <div class="abs s-word" style="top:317px">TUDY</div>
  <div class="abs s-word" style="top:340px">UMMARY</div>
  <p class="abs summary" style="top:183px">Ankle fractures are very common, and often require an operation. After surgery for ankle fracture, patients are usually advised to avoid walking for 6 weeks (delayed weight-bearing). An alternative is to walk 2 weeks after surgery (early weight-bearing).</p>
  <p class="abs summary" style="top:250px">In this study, half of the patients were instructed that they should put as much weight through their affected leg as they felt comfortable and without causing pain. The other half were instructed to avoid putting any weight through their operated leg for six weeks after surgery.</p>
  <p class="abs summary" style="top:317px">After 4 months, ankle function was similar, and the number of complications was similar, in the two groups. The cost to the NCS and social services were also similar, with slightly lower costs in the early weight-bearing group.</p>

  <svg class="wave" style="top:380px" viewBox="0 0 581 6"><rect width="581" height="6" fill="url(#scallop-blue)"/></svg>
  <section class="abs key-band"></section>
  <svg class="wave" style="top:484px;transform:scaleY(-1)" viewBox="0 0 581 6"><rect width="581" height="6" fill="url(#scallop-blue)"/></svg>
  <div class="abs key-row"><span class="key-box">KEY MESSAGES</span><span class="key-findings">FINDINGS</span></div>
  <p class="abs key-text">An early weight-bearing strategy is not inferior in terms of ankle function to a delayed weight-bearing strategy. Early weight-bearing is also likely to be cost-effective.</p>

  <h3 class="abs elig-title">ELIGIBILITY<br>CRITERIA</h3>
  <div class="abs elig-illus" role="img" aria-label="Illustration of three people with a tick badge"></div>
  <div class="abs elig-tag">(IF RELEVANT)</div>
  <div class="abs side-bar" style="left:116px;top:513px;height:122px"><span>INCLUSION CRITERIA</span></div>
  <ul class="criteria">
    <li style="left:139px;top:511px">Aged 18 or over</li>
    <li style="left:139px;top:529px">Has had operative fixation for an<br>unstable ankle fracture.</li>
    <li style="left:139px;top:558px">Surgery was performed within 14 days<br>of the injury.</li>
    <li style="left:139px;top:588px">The treating surgeon considers that<br>the participant might benefit from<br>early weight-bearing.</li>
    <li style="left:139px;top:629px">Able and willing to give informed consent</li>
  </ul>
  <div class="abs side-bar" style="left:334px;top:512px;height:123px"><span>EXCLUSION CRITERIA</span></div>
  <ul class="criteria">
    <li style="left:357px;top:509px">A lack of protective sensation<br>(e.g. peripheral neuropathy).</li>
    <li style="left:357px;top:539px">Inability to adhere to trial procedures.</li>
    <li style="left:357px;top:557px">Bilateral operatively treated ankle<br>fractures.</li>
    <li style="left:357px;top:587px">Already in a trial for ankle fracture.</li>
    <li style="left:357px;top:605px">Patient has received a hindfoot nail to<br>treat index fracture.</li>
  </ul>

  <svg class="wave" style="top:661px" viewBox="0 0 581 6"><rect width="581" height="6" fill="url(#scallop-grey)"/></svg>
  <section class="abs details-band"></section>
  <svg class="wave" style="top:762px;transform:scaleY(-1)" viewBox="0 0 581 6"><rect width="581" height="6" fill="url(#scallop-grey)"/></svg>
  <div class="abs details-illus" role="img" aria-label="Illustration of a study document on a screen"></div>
  <h3 class="abs details-title">STUDY<br>DETAILS</h3>
  <div class="abs details-tag">INCLUSION CRITERIA &nbsp;(IF RELEVANT )</div>
  <ul class="criteria details-list">
    <li style="left:272px;top:674px">Randomised controlled trial</li>
    <li style="left:272px;top:692px">561 adults recruited from 23 NCS hospitals in the UK</li>
    <li style="left:272px;top:708px">A non-inferiority study</li>
    <li style="left:272px;top:727px">Ankle function, quality of life and complications were collected<br>at 6 weeks, 4 months and 12 months after surgery.</li>
  </ul>

  <div class="abs info-card" style="left:28px">
    <div class="info-main">PATIENTS,<br>CLINICIANS</div>
    <div class="info-label">TARGET &nbsp;AUDIENCE</div>
  </div>
  <div class="abs info-circle" style="left:75px" role="img" aria-label="Audience icon"></div>

  <div class="abs info-card" style="left:218px">
    <div class="info-main contact">qrvteam<br>@<br>caddering.ac.example</div>
    <div class="info-label">CONTACT INFORMATION</div>
  </div>
  <div class="abs info-circle" style="left:265px">
    <svg width="26" height="20" viewBox="0 0 26 20" aria-hidden="true"><rect x="1" y="1" width="24" height="18" rx="1.5" fill="none" stroke="#fff" stroke-width="1.6"/><path d="M1.5 2 L13 11 L24.5 2" fill="none" stroke="#fff" stroke-width="1.6"/></svg>
  </div>

  <div class="abs info-card" style="left:411px">
    <div class="info-main">THE UNIVERSITY<br>OF CADDERING</div>
    <div class="info-label">SPONSOR NAME</div>
  </div>
  <div class="abs info-circle" style="left:458px"></div>

  <svg class="wave" style="top:954px" viewBox="0 0 581 6"><rect width="581" height="6" fill="url(#scallop-blue)"/></svg>
  <footer class="abs funding-band"></footer>
  <svg class="wave" style="top:1018px;transform:scaleY(-1)" viewBox="0 0 581 6"><rect width="581" height="6" fill="url(#scallop-blue)"/></svg>
  <p class="abs funding-text">National Institute for Care Studies, Patient Outcomes Grant scheme<br>(PO-GS-4821-30517), supported by the NICS Caddering Biomedical Research Centre</p>

  <div class="abs partner" style="left:32px;top:1040px"><span class="mark"></span>Brindlemoor Injury and Acute Care</div>
  <div class="abs partner uni" style="left:357px;top:1033px"><span class="mark"></span></div>
  <div class="abs partner qrv" style="left:413px;top:1032px"><span class="mark"></span>QRV</div>
</main>
</body>
</html>
```